VENTURE CAPITAL GROUP BUSINESS CARD DESIGN

Venture Capital Group based in SF looking for a bold business card design. No trendy colour explosion, 3D effects etc. Just "simple" optical effects. Works on your brain, keeps your eye focused and sticks to your mind.
Target Market(s)
Technology startups
Industry/Entity Type
Venture Capital
Contact Information for Business Card
BARNABY WHITLOCK
MANAGING PARTNER
817 FERN ST SAN FRANCISCO, CA 94111
415.555.0143 O
415.555.0167 F
415.555.0192 C
barn@halcyonridgefund.example

```html
<!DOCTYPE html>
<html lang="en">
<head>
<meta charset="utf-8">
<title>Halcyon Ridge Capital Group – Business Card</title>
<link href="https://fonts.googleapis.com/css2?family=Roboto:wght@300;400;700&display=swap" rel="stylesheet">
<style>
  :root {
    --bg: #e9e9e7;
    --card: #ffffff;
    --green: #6cb52d;
    --green-dark: #1f8a3a;
    --band-grey: #d9d9d9;
    --swoosh-dark: #3a3a3a;
    --ink: #444444;
    --ink-soft: #8a8a8a;
    --emblem: #e3e3e3;
  }
  * { margin: 0; padding: 0; box-sizing: border-box; }
  html, body { width: 1200px; height: 799px; overflow: hidden; background: var(--bg); }
  body { position: relative; font-family: "Roboto", Arial, sans-serif; }

  .card {
    position: absolute;
    width: 540px;
    height: 309px;
    background: var(--card);
    overflow: hidden;
    box-shadow: 0 6px 18px rgba(0,0,0,0.18);
  }
  .card--front { left: 600px; top: 70px; }
  .card--back { left: 60px; top: 420px; }
  .card__shapes { position: absolute; inset: 0; width: 540px; height: 309px; }

  .brand { position: absolute; text-align: center; }
  .brand__emblem {
    display: block;
    margin: 0 auto 10px;
    border-radius: 50%;
    background: radial-gradient(circle at 40% 35%, #ffffff 0%, var(--emblem) 70%, #cfcfcf 100%);
  }
  .brand__name {
    color: var(--green-dark);
    font-weight: 400;
    text-transform: uppercase;
    letter-spacing: 1px;
    line-height: 1.15;
  }
  .card--front .brand { left: 0; right: 0; top: 40px; }
  .card--front .brand__emblem { width: 92px; height: 92px; }
  .card--front .brand__name { font-size: 26px; }

  .card--back .brand { left: 25px; top: 55px; width: 190px; }
  .card--back .brand__emblem { width: 70px; height: 70px; margin-bottom: 8px; }
  .card--back .brand__name { font-size: 19px; }

  .person { position: absolute; right: 70px; top: 86px; text-align: right; }
  .person__name { font-size: 21px; font-weight: 700; color: var(--ink); letter-spacing: 0.3px; }
  .person__title { font-size: 9px; color: var(--ink-soft); text-transform: uppercase; margin-top: 1px; }

  .contact { position: absolute; font-size: 10px; color: var(--ink-soft); line-height: 1.3; text-transform: uppercase; }
  .contact--phones { right: 78px; top: 136px; text-align: right; }
  .contact--address { right: 78px; top: 182px; text-align: right; }
  .contact--email { left: 160px; top: 214px; text-transform: none; }

  .icon {
    position: absolute;
    width: 22px; height: 22px;
    border: 2px solid var(--green);
    border-radius: 5px;
    display: flex; align-items: center; justify-content: center;
    background: #fff;
  }
  .icon svg { width: 13px; height: 13px; fill: var(--ink); }
  .icon--phone { right: 44px; top: 136px; }
  .icon--home { right: 44px; top: 178px; }
  .icon--mail { left: 292px; top: 150px; }
</style>
</head>
<body>

<section class="card card--front" aria-label="Card front">
  <svg class="card__shapes" viewBox="0 0 540 309" aria-hidden="true">
    <path d="M190,309 Q380,215 540,196 L540,222 Q420,248 300,309 Z" fill="var(--band-grey)"/>
    <path d="M300,309 Q420,248 540,222 L540,309 Z" fill="var(--green)"/>
  </svg>
  <div class="brand">
    <span class="brand__emblem"></span>
    <p class="brand__name">Halcyon Ridge<br>Capital Group</p>
  </div>
</section>

<section class="card card--back" aria-label="Card back">
  <svg class="card__shapes" viewBox="0 0 540 309" aria-hidden="true">
    <path d="M110,0 H540 V48 Q340,18 110,0 Z" fill="var(--green)"/>
    <path d="M290,30 Q440,28 540,48 V74 Q440,46 290,30 Z" fill="var(--swoosh-dark)"/>
    <path d="M0,232 Q230,218 430,309 H385 Q205,250 0,262 Z" fill="var(--band-grey)"/>
    <path d="M0,262 Q205,250 385,309 H0 Z" fill="var(--green)"/>
  </svg>

  <div class="brand">
    <span class="brand__emblem"></span>
    <p class="brand__name">Halcyon Ridge<br>Capital Group</p>
  </div>

  <div class="person">
    <h1 class="person__name">BARNABY WHITLOCK</h1>
    <p class="person__title">Managing Partner</p>
  </div>

  <p class="contact contact--phones">415.555.0143 O<br>415.555.0167 F<br>415.555.0192 C</p>
  <p class="contact contact--address">817 Fern St San Francisco,<br>CA 94111</p>
  <p class="contact contact--email">barn@halcyonridgefund.example</p>

  <span class="icon icon--phone"><svg viewBox="0 0 24 24"><path d="M6.6 10.8a15 15 0 0 0 6.6 6.6l2.2-2.2a1 1 0 0 1 1-.25 11.4 11.4 0 0 0 3.6.57 1 1 0 0 1 1 1V20a1 1 0 0 1-1 1A17 17 0 0 1 3 4a1 1 0 0 1 1-1h3.5a1 1 0 0 1 1 1c0 1.25.2 2.45.57 3.57a1 1 0 0 1-.25 1z"/></svg></span>
  <span class="icon icon--home"><svg viewBox="0 0 24 24"><path d="M12 3 2 12h3v8h5v-6h4v6h5v-8h3z"/></svg></span>
  <span class="icon icon--mail"><svg viewBox="0 0 24 24"><path d="M3 5h18v14H3z M4.5 6.5 12 12l7.5-5.5" fill="none" stroke="#444" stroke-width="2"/></svg></span>
</section>

</body>
</html>
```